QuarryNest - Webstartup looking for some style

QuarryNest is a cloud based web application that allows construction sub-contractors to create and manage bids. Generally, these contractors will contact subcontractors to have them do specific parts of a larger construction project. This would be used by various subcontractors including woodwork (cabinetry), electricians, masons, etc...

Nearly all competitors are clients applications that have to be installed on the computer and are very expensive. This is a much lower cost alternative.

The business is just beginning and we want people to view us as a fresh alternative to companies that have been around for a long time and are starting to look a little dated.

We would like our logo included on the card (see attached). We have been using the circular 'qn' emblem seperately from the complete logo in various areas of the website. We lean towards a professional and clean look, with a tendancy more towards modern.

We want to differentiate ourselves from our competition which tend to be dated, complicated and less graphical.

(We are currently designing our public website as well - but don't have any designs yet)

Industry/Entity Type

Construction

Requirements
Must have
• Circular 'qn' emblem from logo. Probably entire logo, but not necessarily.

Should have reference to website: www.quarrynest-demo.net

The Url should be all lowercase (www.quarrynest-demo.net)
Should not have
• we do not want to list a phone number or email address on the cards. we want people to go to the actual website. we haven't decided if we want names printed on the business cards.

```html
<!DOCTYPE html>
<html lang="en">
<head>
<meta charset="utf-8">
<title>QuarryNest Business Card</title>
<link rel="stylesheet" href="https://fonts.googleapis.com/css2?family=Questrial&family=PT+Sans:wght@700&family=Libre+Baskerville&display=swap">
<style>
  :root {
    --backdrop: #7a4a24;
    --card: #fbf5cc;
    --card-edge: #2b2418;
    --brand-blue: #2e9bd8;
    --brand-orange: #f59a23;
    --ink: #35301f;
  }
  * { margin: 0; padding: 0; box-sizing: border-box; }
  html, body {
    width: 1200px;
    height: 960px;
    overflow: hidden;
  }
  body {
    background: var(--backdrop);
    display: flex;
    flex-direction: column;
    align-items: center;
    justify-content: center;
    gap: 60px;
  }
  .card {
    position: relative;
    width: 700px;
    height: 380px;
    background: var(--card);
    border: 1.5px solid var(--card-edge);
    border-radius: 14px;
    box-shadow: 3px 4px 10px rgba(0, 0, 0, 0.35);
  }
  .corner-mark {
    position: absolute;
    top: 24px;
    left: 24px;
    width: 44px;
    height: 44px;
    border-radius: 50%;
    background: var(--brand-blue);
  }
  .brand-lockup {
    position: absolute;
    left: 150px;
    top: 120px;
    display: flex;
    align-items: center;
    gap: 22px;
  }
  .brand-dot {
    width: 110px;
    height: 110px;
    border-radius: 50%;
    background: var(--brand-orange);
    flex: none;
  }
  .brand-text {
    display: flex;
    flex-direction: column;
  }
  .brand-name {
    font-family: "Questrial", sans-serif;
    font-size: 72px;
    line-height: 1;
    color: var(--brand-blue);
    letter-spacing: -1px;
  }
  .tagline {
    font-family: "PT Sans", sans-serif;
    font-weight: 700;
    font-size: 20px;
    color: var(--ink);
    margin-top: 6px;
    white-space: nowrap;
  }
  .web-address {
    position: absolute;
    right: 28px;
    bottom: 28px;
    font-family: "Libre Baskerville", serif;
    font-size: 20px;
    color: var(--ink);
    letter-spacing: 0.5px;
  }
  .card-back {
    display: flex;
    align-items: center;
    justify-content: center;
  }
  .emblem-circle {
    width: 230px;
    height: 230px;
    border-radius: 50%;
    background: var(--brand-orange);
  }
</style>
</head>
<body>
  <section class="card card-front">
    <span class="corner-mark"></span>
    <div class="brand-lockup">
      <span class="brand-dot"></span>
      <div class="brand-text">
        <span class="brand-name">QuarryNest</span>
        <span class="tagline">Simple Bids for Every Trade Crew</span>
      </div>
    </div>
    <p class="web-address">www.quarrynest-demo.net</p>
  </section>

  <section class="card card-back">
    <span class="emblem-circle"></span>
  </section>
</body>
</html>
```